Yacht Charter Broker needs a magazine page design

We are a travel agent for yachts called Velmoria Yacht Charters. www.velmoriacharters.example We are advertising in a magazine at the grand pacer equine fair - https://plgequinefair.example/ - and need a high-end luxury feeling magazine page.

Target Market(s)

Vacation goers looking to charter a crewed yacht.

Industry/Entity Type

Travel Agent

Requirements
Must have
• luxury feel. logo. website and social media icons if you feel necessary. Our motto is: Inhale. Exhale. Sail.
• Catamaran picture, snorkeling and other island, water looking pictures.
Nice to have
• Open to your design.
Should not have
• Nothing comes to mind.

```html
<!DOCTYPE html>
<html lang="en">
<head>
<meta charset="UTF-8">
<title>Velmoria Yacht Charters – Magazine Page</title>
<link rel="stylesheet" href="https://fonts.googleapis.com/css2?family=Dancing+Script:wght@700&family=Montserrat:wght@300;400;500&display=swap">
<style>
  :root {
    --backdrop: #8d8f8e;
    --sky: #c9d3de;
    --sail: #dfe6ee;
    --hull: #c7d3e0;
    --sea-light: #3a5f8f;
    --sea-mid: #1f3f6e;
    --sea-deep: #0f2347;
    --ink-navy: #1c2a4a;
    --white: #ffffff;
    --white-soft: rgba(255,255,255,0.75);
  }
  * { margin: 0; padding: 0; box-sizing: border-box; }
  html, body {
    width: 1200px;
    height: 863px;
    overflow: hidden;
    background: var(--backdrop);
  }
  .canvas {
    position: relative;
    width: 1200px;
    height: 863px;
    display: flex;
    align-items: center;
    justify-content: center;
  }
  .magazine-page {
    position: relative;
    width: 640px;
    height: 829px;
    overflow: hidden;
    font-family: "Montserrat", sans-serif;
    color: var(--white);
  }
  .hero-photo {
    position: absolute;
    inset: 0;
    background:
      radial-gradient(ellipse 34% 30% at 30% 14%, var(--sail) 0%, rgba(223,230,238,0.6) 55%, rgba(223,230,238,0) 100%),
      radial-gradient(ellipse 44% 13% at 36% 47%, var(--hull) 0%, rgba(199,211,224,0.55) 60%, rgba(199,211,224,0) 100%),
      radial-gradient(ellipse 22% 6% at 26% 58%, rgba(255,255,255,0.55) 0%, rgba(255,255,255,0) 100%),
      linear-gradient(180deg,
        #5c7597 0%,
        #8ea3bc 18%,
        var(--sky) 28%,
        var(--sea-light) 34%,
        var(--sea-mid) 55%,
        var(--sea-deep) 100%);
  }
  .brand {
    position: absolute;
    top: 70px;
    right: 44px;
    text-align: right;
    color: var(--ink-navy);
  }
  .brand-name {
    display: flex;
    align-items: center;
    justify-content: flex-end;
    gap: 12px;
    font-weight: 300;
    font-size: 40px;
    letter-spacing: 7px;
  }
  .brand-mark {
    width: 14px;
    height: 14px;
    border-radius: 50%;
    background: var(--ink-navy);
  }
  .brand-tagline {
    margin-top: 4px;
    font-weight: 400;
    font-size: 9px;
    letter-spacing: 3.5px;
    text-transform: uppercase;
  }
  .ad-copy {
    position: absolute;
    left: 50px;
    right: 50px;
    top: 545px;
    text-align: center;
  }
  .lead-line {
    font-weight: 500;
    font-size: 17px;
    letter-spacing: 1.5px;
    text-transform: uppercase;
  }
  .headline {
    font-family: "Dancing Script", cursive;
    font-weight: 700;
    font-size: 104px;
    line-height: 1;
    margin-top: -2px;
  }
  .rule {
    height: 1px;
    background: var(--white-soft);
    margin: 0 10px;
  }
  .website {
    font-weight: 400;
    font-size: 23px;
    padding: 8px 0 10px;
    letter-spacing: 0.3px;
  }
  .social-row {
    display: flex;
    justify-content: center;
    gap: 6px;
    margin-top: 12px;
  }
  .social-row span {
    width: 24px;
    height: 24px;
    border-radius: 50%;
    background: var(--white);
  }
  .motto {
    margin-top: 12px;
    font-weight: 300;
    font-size: 12px;
    letter-spacing: 4px;
    text-transform: uppercase;
    color: var(--white-soft);
  }
</style>
</head>
<body>
<div class="canvas">
  <article class="magazine-page">
    <div class="hero-photo" role="img" aria-label="Photograph of a white sailing yacht's bow with full sail cutting through deep blue open sea under a pale sky"></div>

    <header class="brand">
      <div class="brand-name"><span class="brand-mark"></span>VELMORIA</div>
      <div class="brand-tagline">Yacht Charter Broker</div>
    </header>

    <section class="ad-copy">
      <p class="lead-line">We have the perfect yacht for your next</p>
      <h1 class="headline">Adventure.</h1>
      <div class="rule"></div>
      <p class="website">www.velmoriacharters.example</p>
      <div class="rule"></div>
      <div class="social-row" aria-label="Social media">
        <span></span><span></span><span></span><span></span>
      </div>
      <p class="motto">Inhale. Exhale. Sail.</p>
    </section>
  </article>
</div>
</body>
</html>
```